Exciting Poster Project: 4 posters for Employee Benefit Program

We are an entrepreneurial healthcare IT company that is creating an internal campaign to launch our 2017 Culture and Professional Development goals for our internal staff.

We need 4 posters utilizing the 4 campaign logos (attached) that are tied together visually into a cohesive campaign.

A PPT is included that shows the other wall art that currently exists on the walls. The new posters will share a space with these pieces.

The posters may be mounted side by side, or stand alone on a wall- so the design should work both ways. Each poster should include its own icon and the tag line provided along with topics provided that fall under this category. The posters size can be dictated by your design, but the text should be legible from a minimum of 8 feet away.

At the bottom of each poster should include all 4 icons in order to tie the entire campaign together (perhaps they can be arranged together like a diamond shape with the primary one as the biggest diamond)

Our company website for our external branding is: www.pelmaroq.com
We have included our branding guidelines for our external brand, and ppts and graphics for our internal brand.

1) Poster 1:
a. Header: Better Today Than Yesterday
b. Sub-title: Personal and Professional Growth
c. Description: We are committed to helping you build on your strengths and passions and support you your career advancement goals. We have a variety of training and development programs available to help you reach your top potential!
Leadership Development Programs
1. Supervisor Training
2. Women’s Leadership
3. Leadership Meet-Ups
4. MBA Program
Staff Development
1. Continuing Education Fund
2. Book Club
3. Pelmaroq University
4. Mentorship
5. Learning Libraries
6. Department Wide Training Events

2) Poster 2:
a. Header: Perform at Highest Capacity
b. Sub-title: Be Your Best Self
c. Description: We are committed to providing programs that bring focus to your health and overall personal wellness to encourage a well balanced life
i. Healthy Living
1. Health and wellness seminars
2. Nutrition: Fruit Delivery
ii. Fitness:
1. Step Challenge
2. Virtual 5k
3. Recess
4. Golf Lessons
5. Ping Pong Club
iii. Creativity:
1. Painting
2. Photography Club
3. Virtual Trivia
iv. Mental Health:
1. Massage Therapy
2. EAP Education
v. Financial
1. 401(k)
2. Retirement education/financial planning seminars
3. Global Insurance Program education

3) Poster 3:
a. Header: Passionate Urgent and Driven to Success
b. Sub-Header: Innovation and Strategy
c. Description: We are committed to helping you connect the dots both in the industry and with our internal goals , mission, and vision.
i. Quarterly All-Hands
ii. Lumiverse
1. Internally: Departmental and Product Updates
2. Externally: Industry Knowledge
3. Culturally: Peer to Peer Community

4) Poster 4:
a. Header: Succeed as a Team
b. Sub-Header: Cultivating Collaboration
c. Description: We are committed to creating a culture of appreciation, teamwork, and supporting an open communication. All feedback and ideas are welcome here!
i. Team Building Events
1. Employee Focused
a. Summer Picnic
b. Employee Appreciation
c. Diwali
d. Holiday Party
e. Department Appreciation
2. Family Friendly
a. Halloween
b. Bring your Kids to Work Day
3. Awards
a. Peer to Peer: QuickNod Awards
b. Leadership: Crest of Merit
4. Surveys
a. New Hire
b. Employee Engagement
Updates

Target Market(s)

Internal Employees

Industry/Entity Type

Healthcare

Font styles to use
Sans Serif

Requirements
Must have
• Job Type: Posters
• Task Outline: Create Vector Art for 4 icons and 4 posters
• Fonts and Styles to Use: SourceSansPro
Nice to have
• There is an attachment with suggested concepts and styles that we like.
Should not have
• The poster should not be very wordy or hard to read in passing.

```html
<!DOCTYPE html>
<html lang="en">
<head>
<meta charset="utf-8">
<title>Succeed as a Team – Cultivating Collaboration</title>
<link rel="stylesheet" href="https://fonts.googleapis.com/css2?family=Fira+Sans+Condensed:wght@700&family=Source+Sans+3:wght@400;700;800&display=swap">
<style>
  :root {
    --backdrop: #96979b;
    --paper: #ffffff;
    --orange: #f2a03a;
    --crimson: #a52834;
    --blue: #1a5fb8;
    --navy: #1f3a6b;
    --white: #ffffff;
  }
  * { margin: 0; padding: 0; box-sizing: border-box; }
  html, body { width: 960px; height: 1200px; overflow: hidden; }
  body { background: var(--backdrop); font-family: "Source Sans 3", sans-serif; position: relative; }
  .poster { position: absolute; left: 160px; top: 160px; width: 640px; height: 880px; background: var(--paper); overflow: hidden; }
  .headline { position: absolute; top: 72px; left: 0; width: 100%; text-align: center; font-family: "Fira Sans Condensed", sans-serif; font-weight: 700; font-size: 68px; letter-spacing: -0.5px; color: var(--orange); line-height: 1; }
  .subhead { position: absolute; top: 165px; left: 0; width: 100%; text-align: center; font-weight: 800; font-size: 26px; color: var(--blue); letter-spacing: 0.2px; }
  .band { position: absolute; top: 263px; left: 0; width: 100%; height: 250px; background: var(--crimson); }
  .campaign-icon { position: absolute; left: 45px; top: 235px; width: 285px; height: 285px; }
  .program-badge { position: absolute; left: 425px; top: 222px; width: 120px; height: 120px; border-radius: 50%; background: var(--crimson); border: 5px solid var(--orange); color: var(--white); text-align: center; display: flex; flex-direction: column; justify-content: center; font-weight: 800; }
  .program-badge .year { font-size: 18px; line-height: 1.1; }
  .program-badge .label { font-size: 11px; line-height: 1.2; text-transform: uppercase; }
  .mission { position: absolute; left: 355px; top: 358px; width: 258px; color: var(--white); font-size: 16.5px; line-height: 23px; text-align: justify; }
  .topics { position: absolute; top: 562px; left: 73px; display: flex; }
  .topic-column { width: 228px; }
  .topic-column + .topic-column { border-left: 3px solid var(--orange); padding-left: 22px; margin-left: 0; width: 300px; }
  .topic-heading { font-weight: 800; font-size: 23px; line-height: 24px; color: var(--blue); text-transform: uppercase; }
  .topic-list { list-style: none; margin-bottom: 2px; }
  .topic-list li { color: var(--crimson); font-size: 18px; line-height: 22px; }
  .footer-rule { position: absolute; left: 40px; top: 808px; width: 448px; height: 2px; background: var(--orange); }
  .brand { position: absolute; top: 822px; display: flex; align-items: center; gap: 8px; font-weight: 800; font-size: 28px; color: var(--navy); letter-spacing: -0.5px; }
  .brand .mark { width: 26px; height: 26px; }
  .brand-primary { left: 40px; }
  .brand-primary .mark { background: #e9582b; }
  .brand-secondary { left: 225px; }
  .brand-secondary .mark { background: #1f6fc0; }
  .campaign-set { position: absolute; left: 498px; top: 758px; width: 108px; height: 104px; }
</style>
</head>
<body>
  <main class="poster">
    <h1 class="headline">SUCCEED AS A TEAM</h1>
    <h2 class="subhead">CULTIVATING COLLABORATION</h2>

    <div class="band"></div>

    <svg class="campaign-icon" viewBox="0 0 285 285" role="img" aria-label="Collaboration campaign icon">
      <defs>
        <linearGradient id="iconTone" x1="0" y1="0" x2="1" y2="1">
          <stop offset="0" stop-color="#f5ad4c"/>
          <stop offset="1" stop-color="#ee9630"/>
        </linearGradient>
      </defs>
      <rect x="22" y="22" width="241" height="241" rx="40" fill="url(#iconTone)"/>
    </svg>

    <div class="program-badge">
      <span class="year">2017</span>
      <span class="label">Culture and<br>Professional<br>Development<br>Program</span>
    </div>

    <p class="mission">We are committed to creating a culture of appreciation, teamwork, and supporting an open communication. All feedback and ideas are welcome here!</p>

    <section class="topics">
      <div class="topic-column">
        <h3 class="topic-heading">Team Building<br>Events</h3>
        <ul class="topic-list">
          <li>Employee Focused</li>
          <li>Summer Picnic</li>
          <li>Employee Appreciation</li>
          <li>Diwali</li>
          <li>Holiday Party</li>
          <li>Department Appreciation</li>
        </ul>
      </div>
      <div class="topic-column">
        <h3 class="topic-heading">Family Friendly</h3>
        <ul class="topic-list">
          <li>Halloween</li>
          <li>Bring your Kids to Work Day</li>
        </ul>
        <h3 class="topic-heading">Awards</h3>
        <ul class="topic-list">
          <li>Peer to Peer: QuickNod Awards</li>
          <li>Leadership: Crest of Merit</li>
        </ul>
        <h3 class="topic-heading">Surveys</h3>
        <ul class="topic-list">
          <li>New Hire&nbsp; l&nbsp; Employee Engagement</li>
        </ul>
      </div>
    </section>

    <div class="footer-rule"></div>
    <div class="brand brand-primary"><span class="mark"></span>Pelmaroq</div>
    <div class="brand brand-secondary"><span class="mark"></span>Stitchway</div>

    <svg class="campaign-set" viewBox="0 0 108 104" role="img" aria-label="The four campaign icons grouped together">
      <defs>
        <linearGradient id="setTone" x1="0" y1="0" x2="1" y2="1">
          <stop offset="0" stop-color="#f2a03a"/>
          <stop offset="0.4" stop-color="#7b3f98"/>
          <stop offset="0.7" stop-color="#2f8ea8"/>
          <stop offset="1" stop-color="#7dc242"/>
        </linearGradient>
      </defs>
      <rect x="6" y="6" width="96" height="92" rx="12" fill="url(#setTone)"/>
    </svg>
  </main>
</body>
</html>
```